Velquora Design
Would like the design to go over the page in a way that can type over it.
We are a personal training and small group studio
Want it to be professional and classy
Updates
Project Deadline Extended
Reason: Asked for some modifications on a few designs, want to give the designers time to do this
Target Market(s)
All age groups, sports professionals as well as business professionals, families
Industry/Entity Type
Training
Requirements
Must have
- Must have Velquora Studio
Mina Tellaver
214 Barnicot Lane
Wexcombe Vale
South Australia 5173
Phone: 0438917263
Nice to have
- Professional classy fonts
Colour
Should not have
- Clip art
Balloons

```html
<!DOCTYPE html>
<html lang="en">
<head>
<meta charset="utf-8">
<title>Velquora Studio Letterhead</title>
<link href="https://fonts.googleapis.com/css2?family=Open+Sans:wght@400;600;700&display=swap" rel="stylesheet">
<style>
  :root {
    --paper: #ffffff;
    --brand-blue: #1e63c0;
    --accent-cyan: #12a7e0;
    --accent-orange: #f26a1b;
    --band-navy: #1b3f9c;
    --band-cyan: #09c4f5;
    --text-grey: #3b3b3b;
    --rule-grey: #9a9a9a;
    --mark-faint: #efefef;
  }
  * { margin: 0; padding: 0; box-sizing: border-box; }
  html, body { width: 956px; height: 1200px; overflow: hidden; background: var(--paper); }
  .letterhead {
    position: relative;
    width: 956px;
    height: 1200px;
    background: var(--paper);
    font-family: "Open Sans", Arial, sans-serif;
    color: var(--text-grey);
  }
  .brand {
    position: absolute;
    left: 250px;
    top: 70px;
    display: flex;
    align-items: center;
    gap: 12px;
  }
  .brand-dot {
    width: 22px;
    height: 22px;
    border-radius: 50%;
    background: var(--accent-orange);
  }
  .brand-name {
    font-weight: 700;
    font-size: 30px;
    line-height: 1;
    color: var(--brand-blue);
    letter-spacing: -0.5px;
  }
  .header-rule {
    position: absolute;
    left: 529px;
    top: 56px;
    width: 1.5px;
    height: 96px;
    background: var(--rule-grey);
  }
  .contact {
    position: absolute;
    left: 549px;
    top: 58px;
    font-size: 15px;
    line-height: 1.15;
  }
  .contact-line { margin-bottom: 6px; }
  .contact-label { color: var(--accent-cyan); font-weight: 700; }
  .address { margin-top: 14px; font-size: 14.5px; line-height: 1.12; }
  .faint-mark {
    position: absolute;
    left: 338px;
    top: 420px;
    width: 280px;
    height: 280px;
    border-radius: 50%;
    background: var(--mark-faint);
  }
  .footer-wave {
    position: absolute;
    left: 0;
    bottom: 0;
    width: 956px;
    height: 1200px;
  }
  .footer-text {
    position: absolute;
    left: 91px;
    top: 1136px;
    color: #ffffff;
    font-weight: 700;
    font-size: 15px;
  }
  .footer-company { margin-bottom: 10px; font-size: 16px; }
</style>
</head>
<body>
  <div class="letterhead">
    <div class="brand">
      <span class="brand-dot"></span>
      <span class="brand-name">Velquora Studio</span>
    </div>
    <div class="header-rule"></div>
    <div class="contact">
      <p class="contact-line"><span class="contact-label">Phone</span> : 0438917263</p>
      <p class="contact-line"><span class="contact-label">Email</span> : info@velquora.com</p>
      <p class="address">214 Barnicot Lane<br>Wexcombe Vale<br>South Australia 5173</p>
    </div>

    <div class="faint-mark"></div>

    <svg class="footer-wave" viewBox="0 0 956 1200" aria-hidden="true">
      <defs>
        <linearGradient id="bandGradient" x1="0" y1="0" x2="1" y2="0">
          <stop offset="0" stop-color="var(--band-navy)"/>
          <stop offset="0.45" stop-color="var(--band-cyan)"/>
          <stop offset="1" stop-color="var(--band-navy)"/>
        </linearGradient>
      </defs>
      <path d="M0,1091 C250,1068 500,1140 700,1150 C820,1155 900,1140 956,1118 L956,1128 C900,1150 820,1165 700,1160 C500,1150 250,1082 0,1100 Z" fill="var(--accent-orange)"/>
      <path d="M0,1106 C250,1090 500,1158 700,1168 C820,1172 900,1156 956,1138 L956,1200 L0,1200 Z" fill="url(#bandGradient)"/>
    </svg>

    <div class="footer-text">
      <p class="footer-company">Velquora Studio</p>
      <p class="footer-person">Mina Tellaver</p>
    </div>
  </div>
</body>
</html>
```